Medical supplies company needs a catalogue re-design

Our present catalogue is spread over a number of pages but this needs to be reduced. 4-5 images would require to be on each page. It needs to be professional, simple and elegant. The photos and descriptors need to be adjacent to each other. It should be able to be emailed conventionally as an e-catalogue without it being compressed. an email with existing catalogue will be emailed to anyone interested.
https://www.filevarn.com/s/82kqtb5wzrmuyap/consumables%20photos%20and%20descriptions.pdf?dl=0
Target Market(s)
medical practices, hospitals
Industry/Entity Type
Medical Supply

```html
<!DOCTYPE html>
<html lang="en">
<head>
<meta charset="utf-8">
<title>Instruments – Neva Medical Catalogue</title>
<link href="https://fonts.googleapis.com/css2?family=Arimo:wght@400;700&family=Cinzel:wght@700&display=swap" rel="stylesheet">
<style>
  :root {
    --brand-red: #e0222f;
    --ink: #111111;
    --muted: #555a60;
    --panel: #e9eaeb;
    --panel-edge: #b9bbbe;
    --pack-light: #f7f9fc;
    --pack-shade: #dde4ee;
    --page: #ffffff;
  }
  * { box-sizing: border-box; margin: 0; padding: 0; }
  html, body { width: 929px; height: 1200px; overflow: hidden; background: var(--page); }
  .page { position: relative; width: 929px; height: 1200px; font-family: "Arimo", Arial, sans-serif; }
  .band { position: absolute; left: 0; width: 100%; background: var(--brand-red); }
  .band--top { top: 0; height: 30px; }
  .band--bottom { bottom: 0; height: 41px; }
  .section-title {
    position: absolute; left: 61px; top: 66px;
    font-family: "Cinzel", Georgia, serif; font-weight: 700;
    font-size: 36px; color: var(--brand-red); letter-spacing: 1px;
  }
  .photo {
    position: absolute; border: 1px solid #c9ced6; z-index: 2;
    background: linear-gradient(160deg, var(--pack-light) 0%, var(--pack-shade) 100%);
  }
  .photo--open { background: linear-gradient(160deg, #eef2f7 0%, #c9d3df 100%); }
  .spec {
    position: absolute; z-index: 1;
    background: var(--panel); border: 1px solid var(--panel-edge);
    border-radius: 14px; padding: 10px 12px 10px 48px;
  }
  .spec__name { font-size: 16.5px; font-weight: 400; color: var(--ink); line-height: 1.2; margin-bottom: 4px; }
  .spec__list { list-style: none; }
  .spec__list li {
    position: relative; padding-left: 10px;
    font-size: 13.5px; line-height: 1.3; color: var(--muted);
  }
  .spec__list li::before {
    content: ""; position: absolute; left: 0; top: 7px;
    width: 4px; height: 4px; border-radius: 50%; background: var(--brand-red);
  }
  .brand {
    position: absolute; left: 640px; top: 1030px;
    display: flex; align-items: center; gap: 8px;
    font-weight: 700; font-size: 34px; color: var(--brand-red); letter-spacing: 2px;
  }
  .brand__dot { width: 26px; height: 26px; border-radius: 50%; background: var(--brand-red); }
  .site { position: absolute; left: 629px; top: 1103px; font-size: 14px; color: var(--muted); letter-spacing: 0.5px; }
</style>
</head>
<body>
<main class="page">
  <div class="band band--top"></div>
  <h1 class="section-title">Instruments</h1>

  <!-- Disposable surgical pack -->
  <div class="photo" style="left:65px;top:141px;width:99px;height:180px" role="img" aria-label="Sealed disposable surgical pack, front of packet"></div>
  <div class="photo photo--open" style="left:171px;top:141px;width:114px;height:180px" role="img" aria-label="Surgical pack instruments inside clear blister"></div>
  <section class="spec" style="left:242px;top:148px;width:188px;height:201px;padding-left:48px">
    <h2 class="spec__name">Disposable Surgical Pack</h2>
    <ul class="spec__list">
      <li>Iris Scissors 11.5cm</li>
      <li>Needle holder 12.5cm</li>
      <li>tooth forcep 12.7cm</li>
      <li>paper blister back 10x20cm</li>
    </ul>
  </section>

  <!-- Iris scissors -->
  <div class="photo" style="left:473px;top:144px;width:91px;height:186px" role="img" aria-label="Sealed iris scissors packet"></div>
  <div class="photo photo--open" style="left:568px;top:144px;width:98px;height:186px" role="img" aria-label="Iris scissors in clear pouch"></div>
  <section class="spec" style="left:651px;top:147px;width:231px;height:144px;padding-left:32px">
    <h2 class="spec__name">Iris Scissors 11.5cm</h2>
    <ul class="spec__list">
      <li>Iris Scissors 11.5cm straight</li>
      <li>Stainless Steel</li>
      <li>Sterile</li>
    </ul>
  </section>

  <!-- Halstead mosquito forceps -->
  <div class="photo" style="left:65px;top:371px;width:91px;height:192px" role="img" aria-label="Sealed Halstead mosquito forceps packet"></div>
  <div class="photo photo--open" style="left:164px;top:371px;width:118px;height:192px" role="img" aria-label="Halstead mosquito forceps in clear pouch"></div>
  <section class="spec" style="left:242px;top:389px;width:190px;height:209px;padding-left:48px">
    <h2 class="spec__name">Halstead Mosquito Forceps Straight 14cm</h2>
    <ul class="spec__list">
      <li>Halstead Mosquito Forcep</li>
      <li>14cm Straight</li>
      <li>Stainless Steel</li>
      <li>Sterile</li>
    </ul>
  </section>

  <!-- Tooth forceps Adson -->
  <div class="photo" style="left:473px;top:379px;width:97px;height:247px" role="img" aria-label="Sealed Adson tooth forceps packet"></div>
  <div class="photo photo--open" style="left:577px;top:379px;width:117px;height:247px" role="img" aria-label="Adson tooth forceps in clear pouch"></div>
  <section class="spec" style="left:662px;top:361px;width:230px;height:245px;padding-left:46px">
    <h2 class="spec__name">Tooth Forceps, Dressing and Tissue, Adson 12.5cm</h2>
    <ul class="spec__list">
      <li>Tooth Forceps, Dressing and Tissue, Adson 12.5cm</li>
      <li>Straight</li>
      <li>Stainless Steel</li>
      <li>Sterile</li>
    </ul>
  </section>

  <!-- Splinter forceps -->
  <div class="photo" style="left:73px;top:648px;width:88px;height:205px" role="img" aria-label="Sealed Hunter splinter forceps packet"></div>
  <div class="photo photo--open" style="left:164px;top:648px;width:88px;height:205px" role="img" aria-label="Hunter splinter forceps in clear pouch"></div>
  <section class="spec" style="left:242px;top:706px;width:187px;height:161px;padding-left:38px">
    <h2 class="spec__name">Splinter Forceps; Hunter 11.5cm</h2>
    <ul class="spec__list">
      <li>Splinter Forceps; Hunter 11.5cm Straight</li>
      <li>Stainless Steel</li>
      <li>Sterile</li>
    </ul>
  </section>

  <!-- Forcep dressing fine -->
  <div class="photo" style="left:470px;top:655px;width:112px;height:194px" role="img" aria-label="Sealed fine dressing forcep packet"></div>
  <div class="photo photo--open" style="left:589px;top:655px;width:103px;height:194px" role="img" aria-label="Fine dressing forcep in clear pouch"></div>
  <section class="spec" style="left:667px;top:662px;width:203px;height:198px;padding-left:40px">
    <h2 class="spec__name">Forcep dressing fine 12.5cm</h2>
    <ul class="spec__list">
      <li>Forcep dressing fine 12.5cm</li>
      <li>Straight</li>
      <li>Stainless Steel</li>
      <li>Sterile</li>
    </ul>
  </section>

  <!-- Sharp scissors -->
  <div class="photo" style="left:83px;top:901px;width:100px;height:220px" role="img" aria-label="Sealed sharp scissors packet"></div>
  <div class="photo photo--open" style="left:189px;top:901px;width:120px;height:220px" role="img" aria-label="Sharp scissors in clear pouch"></div>
  <section class="spec" style="left:288px;top:914px;width:182px;height:203px;padding-left:44px">
    <h2 class="spec__name">Sharp Scissors 12.5cm</h2>
    <ul class="spec__list">
      <li>Sharp Scissors 12.5cm</li>
      <li>Straight</li>
      <li>Stainless Steel</li>
      <li>Sterile</li>
    </ul>
  </section>

  <div class="brand"><span>NEVA MEDICAL</span><span class="brand__dot"></span></div>
  <p class="site">www.nevamedical.com.au</p>

  <div class="band band--bottom"></div>
</main>
</body>
</html>
```